Mousepad Design Creation

We need a round mousepad design. It should have a darker, technology look. Maybe a circuit board or AI feel. It will include our logo, tagline (Let's Up Your Game), and contact information (503.627.CALL (2255) and help@brivanode.com. Attached is one of our current mousepads, as well as our white Q logo. We are just looking for a redesign/update.

```html
<!DOCTYPE html>
<html lang="en">
<head>
<meta charset="utf-8">
<title>Brivanode Round Mousepad</title>
<link rel="stylesheet" href="https://fonts.googleapis.com/css2?family=Montserrat:wght@400;800&display=swap">
<style>
  :root {
    --backdrop: #ececec;
    --pad-rim: #f7f7f7;
    --slate: #7b8fb3;
    --navy: #15173f;
    --contact-ink: #d3dbea;
    --white: #ffffff;
    --badge: #8fa1c2;
  }
  html, body {
    margin: 0;
    padding: 0;
    width: 1200px;
    height: 853px;
    overflow: hidden;
    background: var(--backdrop);
  }
  .mousepad {
    display: block;
    width: 1200px;
    height: 853px;
  }
  .pad-rim { fill: var(--pad-rim); }
  .band-upper { fill: var(--slate); }
  .band-lower { fill: var(--navy); }
  .partner-badge { fill: var(--badge); }
  .contact-line {
    font-family: "Montserrat", sans-serif;
    font-weight: 400;
    font-size: 15px;
    letter-spacing: 2px;
    fill: var(--contact-ink);
  }
  .brand-name {
    font-family: "Montserrat", sans-serif;
    font-weight: 800;
    font-size: 54px;
    fill: var(--white);
  }
  .brand-square { fill: var(--white); }
  .tagline {
    font-family: "Montserrat", sans-serif;
    font-weight: 800;
    font-size: 36px;
    letter-spacing: 1px;
    fill: var(--white);
  }
</style>
</head>
<body>
<svg class="mousepad" viewBox="0 0 1200 853" xmlns="http://www.w3.org/2000/svg">
  <defs>
    <clipPath id="pad-shape">
      <circle cx="600" cy="426" r="392"/>
    </clipPath>
    <path id="upper-arc" d="M 270 426 A 330 330 0 0 1 930 426"/>
    <path id="lower-arc" d="M 262 426 A 338 338 0 0 0 938 426"/>
  </defs>

  <circle class="pad-rim" cx="600" cy="426" r="397"/>

  <g class="pad-face" clip-path="url(#pad-shape)" role="img" aria-label="Round pad with a faint circuit board trace pattern over slate and navy bands">
    <rect class="band-upper" x="200" y="30" width="800" height="800"/>
    <path class="band-lower"
          d="M 200 300 C 260 300 290 282 340 282 C 430 282 500 330 600 330 C 700 330 780 282 860 282 C 920 282 960 296 1000 296 L 1000 830 L 200 830 Z"/>
  </g>

  <rect class="partner-badge" x="560" y="92" width="80" height="20" rx="3"/>

  <text class="contact-line"><textPath href="#upper-arc" startOffset="27%" text-anchor="middle">503.627.CALL (2255)</textPath></text>
  <text class="contact-line"><textPath href="#upper-arc" startOffset="73%" text-anchor="middle">help@brivanode.com</textPath></text>

  <g class="brand-logo">
    <rect class="brand-square" x="448" y="448" width="16" height="16"/>
    <text class="brand-name" x="612" y="476" text-anchor="middle">Brivanode</text>
  </g>

  <text class="tagline"><textPath href="#lower-arc" startOffset="50%" text-anchor="middle">LET’S UP YOUR GAME</textPath></text>
</svg>
</body>
</html>
```